Emerging Australian photographer

I'm based in Cunderdin, a small rural town in the Wheatbelt area of Western Australia. So its a good thing that I love to travel further afield both for pleasure and for work. To me that is one and the same thing in any event!

My desire is to take photos that make the viewers heart skip. I love taking photos of people doing the things they love or being with the people they love. For me, the joy of photography comes with capturing the 'moments between the moments'. I like candid photography best of all - like when the new husband is staring joyfully at his bride and at that minute is unaware of the photographer capturing the moment.

I am available for weddings, engagements, birthdays, special events, newborns, family or individual portraits. By the end of the year I will be accredited with the Coastal Guild of Image Artisans.

I need a card that stands out but is elegant and would sit well on the table at a wedding or be given out in the church grounds. Classy and a little bit sassy.

Target Market(s)

Consumers who are seeking photographic services, eg wedding guests who see me at work and make enquiries.

Industry/Entity Type

Church

Contact Information for Business Card

Tamsin Bexley Photography
Tamsin Bexley
0452 307 618
www.tamsinbexley.com.au
photos@tamsinbexley.com.au

Requirements
Must have
• Must fit with the theme in the watermarks, but be crisp and modern.
Nice to have
• However it's not essential to have the pink! Friendlink and Chirpline logos.
Should not have
• Old style fonts like times new roman.

```html
<!DOCTYPE html>
<html lang="en">
<head>
<meta charset="utf-8">
<title>Tamsin Bexley Photography — Business Card</title>
<link rel="stylesheet" href="https://fonts.googleapis.com/css2?family=Quicksand:wght@300;400&display=swap">
<style>
  :root {
    --ink: #6b6c6e;
    --ink-soft: #8a8b8d;
    --paper: #ececec;
    --paper-glow: #ffffff;
    --mark: #6b6c6e;
    --chip: #a39b95;
  }
  * { margin: 0; padding: 0; box-sizing: border-box; }
  html, body { width: 1200px; height: 695px; overflow: hidden; }
  body {
    font-family: "Quicksand", sans-serif;
    color: var(--ink);
    background: var(--paper);
  }
  .card {
    position: relative;
    width: 1200px;
    height: 695px;
    overflow: hidden;
    background: radial-gradient(circle at 600px 348px, var(--paper-glow) 0%, #f6f6f6 35%, var(--paper) 80%);
  }
  .vertical {
    position: absolute;
    white-space: nowrap;
    transform: translate(-50%, -50%) rotate(-90deg);
    line-height: 1;
  }
  .brand-name {
    left: 158px; top: 350px;
    font-size: 86px;
    font-weight: 300;
    letter-spacing: 0;
  }
  .brand-tagline {
    left: 216px; top: 348px;
    font-size: 21px;
    font-weight: 300;
    letter-spacing: 12px;
  }
  .aperture {
    position: absolute;
    left: 317px; top: 114px;
    width: 468px; height: 468px;
  }
  .contact-phone {
    left: 866px; top: 346px;
    font-size: 39px;
    font-weight: 300;
    letter-spacing: 2px;
  }
  .contact-email {
    left: 922px; top: 348px;
    font-size: 40px;
    font-weight: 300;
  }
  .contact-web {
    left: 985px; top: 346px;
    font-size: 23px;
    font-weight: 300;
  }
  .social {
    left: 1096px; top: 348px;
    display: flex;
    align-items: center;
    gap: 28px;
    font-size: 17px;
    font-weight: 400;
    color: var(--ink-soft);
  }
  .social-item { display: flex; align-items: center; gap: 10px; }
  .social-chip {
    width: 34px; height: 34px;
    border-radius: 6px;
    background: var(--chip);
  }
</style>
</head>
<body>
  <main class="card">
    <h1 class="vertical brand-name">Tamsin Bexley</h1>
    <p class="vertical brand-tagline">Photography</p>

    <svg class="aperture" viewBox="0 0 468 468" role="img" aria-label="Camera aperture emblem">
      <circle cx="234" cy="234" r="234" fill="var(--mark)"/>
    </svg>

    <p class="vertical contact-phone">0452 307 618</p>
    <p class="vertical contact-email">photos@tamsinbexley.com.au</p>
    <p class="vertical contact-web">www.tamsinbexley.com.au</p>

    <div class="vertical social">
      <span class="social-item"><span class="social-chip"></span>Chirpline</span>
      <span class="social-item"><span class="social-chip"></span>Friendlink</span>
    </div>
  </main>
</body>
</html>
```